Business card design needed

Need a new business card design for a new business in Sydney, Australia called 'Verrowin Australia'. The business deals in consulting for new sales, sales leadership and customer service consultancy. Want the business card to look professional and clean

Industry/Entity Type

Leadership

Contact Information for Business Card

Verrowin Australia
Tobias Wrenley
Managing Director

14 Quarrion Avenue
Marrowdale NSW 2041

0432 517 806
tobias@verrowin.com.au
www.verrowin.com.au

```html
<!DOCTYPE html>
<html lang="en">
<head>
<meta charset="utf-8">
<title>Verrowin Australia — Business Card</title>
<link href="https://fonts.googleapis.com/css2?family=Open+Sans:wght@400;600;700&display=swap" rel="stylesheet">
<style>
  :root {
    --page-bg: #e9e6e1;
    --card-black: #000000;
    --panel-dark: #3d3d3d;
    --panel-light: #5c5c5c;
    --accent-red: #e3141b;
    --text-white: #ffffff;
    --text-soft: #e4e4e4;
    --silver-dark: #8a8a8e;
    --silver-light: #f2f2f4;
  }
  * { box-sizing: border-box; margin: 0; padding: 0; }
  html, body {
    width: 1200px; height: 1000px; overflow: hidden;
    background: var(--page-bg);
    font-family: "Open Sans", Arial, sans-serif;
  }
  .canvas { position: relative; width: 1200px; height: 1000px; }
  .card {
    position: absolute; top: 350px;
    width: 538px; height: 301px;
    background: var(--card-black);
    box-shadow: 0 6px 18px rgba(0,0,0,0.35);
    overflow: hidden;
  }
  .card--front { left: 45px; }
  .card--back { left: 617px; }

  .silver-edge {
    position: absolute; top: 0; width: 13px; height: 100%;
    background: linear-gradient(90deg, var(--silver-dark), var(--silver-light) 45%, var(--silver-dark));
  }
  .card--front .silver-edge { left: 0; }
  .card--back .silver-edge { right: 0; }

  .name-panel {
    position: absolute; left: 13px; top: 0; width: 255px; height: 100%;
    background: linear-gradient(90deg, var(--panel-light), var(--panel-dark));
    display: flex; flex-direction: column; align-items: center; justify-content: center;
    color: var(--text-white); text-align: center;
  }
  .person-name { font-size: 19px; font-weight: 700; line-height: 1.3; }
  .person-title { font-size: 14px; font-weight: 600; color: var(--text-soft); margin-top: 4px; }

  .divider { position: absolute; left: 264px; top: 0; width: 10px; height: 301px; }

  .contact-list {
    position: absolute; left: 286px; top: 85px;
    list-style: none; color: var(--text-white);
    font-size: 12.5px; font-weight: 600;
  }
  .contact-item { display: flex; align-items: center; height: 17px; margin-bottom: 18px; }
  .contact-item:nth-child(2) { margin-bottom: 20px; }
  .contact-icon { width: 16px; height: 16px; margin-right: 8px; flex: none; fill: var(--text-white); }

  .brand {
    position: absolute; left: 0; right: 13px; top: 125px;
    text-align: center; color: var(--text-white);
    font-size: 31px; font-weight: 700; letter-spacing: 0.2px;
  }
  .brand-underline { position: absolute; left: 120px; top: 166px; width: 292px; height: 10px; }
</style>
</head>
<body>
<main class="canvas">

  <section class="card card--front" aria-label="Business card front">
    <div class="silver-edge"></div>
    <div class="name-panel">
      <p class="person-name">Tobias Wrenley</p>
      <p class="person-title">Managing Director</p>
    </div>
    <svg class="divider" viewBox="0 0 10 301" preserveAspectRatio="none" aria-hidden="true">
      <path d="M4 0 Q7.5 150 4 301 Q5.5 150 4 0 Z" fill="var(--accent-red)" stroke="var(--accent-red)" stroke-width="1.4"/>
    </svg>
    <ul class="contact-list">
      <li class="contact-item">
        <svg class="contact-icon" viewBox="0 0 16 16" aria-hidden="true"><path d="M8 1 L1 7.5 L2.4 8.8 L8 3.6 L13.6 8.8 L15 7.5 Z M3.5 9.2 V15 H6.8 V11 H9.2 V15 H12.5 V9.2 L8 5 Z"/></svg>
        14 Quarrion Avenue Marrowdale NSW 2041
      </li>
      <li class="contact-item">
        <svg class="contact-icon" viewBox="0 0 16 16" aria-hidden="true"><path d="M3.2 1.2 L5.6 1 L7 4.6 L5.4 6 Q6.6 8.8 9.8 10.6 L11.2 9 L14.8 10.4 L14.6 12.8 Q13.8 14.8 11.6 14.6 Q4.2 13 1.4 4.4 Q1.2 2 3.2 1.2 Z"/></svg>
        0432 517 806
      </li>
      <li class="contact-item">
        <svg class="contact-icon" viewBox="0 0 16 16" aria-hidden="true"><path d="M1 3.5 H15 V4.6 L8 9.4 L1 4.6 Z M1 6.2 L8 11 L15 6.2 V13 H1 Z"/></svg>
        tobias@verrowin.com.au
      </li>
      <li class="contact-item">
        <svg class="contact-icon" viewBox="0 0 16 16" aria-hidden="true"><circle cx="8" cy="8" r="6.8" fill="none" stroke="#fff" stroke-width="1.3"/><ellipse cx="8" cy="8" rx="3" ry="6.8" fill="none" stroke="#fff" stroke-width="1.1"/><path d="M1.2 8 H14.8 M2.2 4.8 H13.8 M2.2 11.2 H13.8 M8 1.2 V14.8" stroke="#fff" stroke-width="1.1"/></svg>
        www.verrowin.com.au
      </li>
    </ul>
  </section>

  <section class="card card--back" aria-label="Business card back">
    <h1 class="brand">Verrowin Australia</h1>
    <svg class="brand-underline" viewBox="0 0 292 10" preserveAspectRatio="none" aria-hidden="true">
      <path d="M0 3 Q146 9 292 3 Q146 5.5 0 3 Z" fill="var(--accent-red)" stroke="var(--accent-red)" stroke-width="1.2"/>
    </svg>
    <div class="silver-edge"></div>
  </section>

</main>
</body>
</html>
```